Tandem Roster survey and prize

We need an A4 poster design for a survey and competition I wish to hold. The survey will be on Poll Heron. My website www.TandemRoster.com.au will redirect the users to the survey page. I will be selecting a survey entrant at random to win a prize. The prize is $200 cash. The survey will be open for two months as the mail out of this poster will go throughout Victoria, Australia. The competition end date is yet to be decided - depends on when I can get this poster completed and the mail out done.

The mail out is targeting the Aged Care industry workers and decision makers. It hopefully will be placed on a notice board in the facilities and need to attract attention for people to visit my site and then take the survey.

The survey is for not for residents but for the workers in the facility.

Reason: Just got some feedback on required content of the poster. Text for the poster required: "The survey is for determining a market for rostering and payroll software, your assitance in taking this survey would be greatly appreciated." Martin Hale

Target Market(s)

Workers in Aged Care industry and decision makers.

Industry/Entity Type

Industry

Requirements
Must have
• 1. Must reference the website www.TandemRoster.com.au.
2. Must mention that there is a prize of $200.
3. Must mention that entry to the competition is dependant on taking the survey.
4. Must mention the close date (date yet to be decided).
5. Must mention winning contestant will be contacted by phone.

```html
<!DOCTYPE html>
<html lang="en">
<head>
<meta charset="utf-8">
<title>Tandem Roster – Survey Competition Poster</title>
<link rel="stylesheet" href="https://fonts.googleapis.com/css2?family=League+Gothic&family=Roboto:ital,wght@0,300;0,400;0,500;0,700;1,400;1,900&display=swap">
<style>
  :root {
    --ink: #2f3038;
    --brand-blue: #3f62a1;
    --prize-yellow: #f9d94c;
    --panel-dark: #3a3c48;
    --paper: #ffffff;
    --photo-light: #f4f5f7;
    --photo-mid: #c9cdd4;
    --muted: #55575f;
  }
  html, body {
    margin: 0;
    padding: 0;
    overflow: hidden;
    background: var(--paper);
  }
  .poster {
    position: relative;
    width: 848px;
    height: 1200px;
    overflow: hidden;
    background: var(--paper);
    font-family: "Roboto", Arial, sans-serif;
  }
  .poster-art {
    position: absolute;
    inset: 0;
  }
  .headline text {
    font-family: "League Gothic", "Arial Narrow", sans-serif;
  }
  .headline .dark { fill: var(--ink); }
  .headline .blue { fill: var(--brand-blue); }
  .headline-rule { stroke: var(--brand-blue); stroke-width: 2.5; }
  .prize-text {
    font-family: "Roboto", Arial, sans-serif;
    font-style: italic;
    font-weight: 900;
  }
  .survey-purpose {
    position: absolute;
    left: 97px;
    top: 758px;
    width: 256px;
    margin: 0;
    font-size: 12.5px;
    line-height: 16px;
    color: var(--muted);
  }
  .survey-purpose__sign {
    font-style: italic;
    font-weight: 500;
    color: var(--ink);
  }
  .survey-panel {
    position: absolute;
    left: 53px;
    top: 855px;
    width: 346px;
    height: 261px;
    border-radius: 32px;
    background: var(--panel-dark);
    color: var(--paper);
    text-align: center;
  }
  .survey-panel__intro {
    margin: 0;
    padding-top: 44px;
    font-weight: 300;
    font-size: 29px;
    line-height: 39px;
  }
  .survey-panel__url {
    margin: 38px 0 0;
    font-weight: 500;
    font-size: 24px;
    letter-spacing: -0.2px;
  }
  .closing {
    position: absolute;
    right: 50px;
    top: 1080px;
    text-align: right;
    color: #000;
  }
  .closing__date {
    margin: 0;
    font-size: 30px;
    font-weight: 400;
    line-height: 36px;
  }
  .closing__date strong { font-weight: 500; }
  .closing__note {
    margin: 4px 0 0;
    font-size: 16px;
    font-weight: 400;
  }
  .footer-band {
    position: absolute;
    left: 0;
    bottom: 0;
    width: 848px;
    height: 34px;
    background: var(--brand-blue);
  }
</style>
</head>
<body>
<main class="poster">
  <svg class="poster-art" width="848" height="1200" viewBox="0 0 848 1200">
    <defs>
      <linearGradient id="photoTone" x1="0" y1="0" x2="1" y2="1">
        <stop offset="0" stop-color="var(--photo-light)"/>
        <stop offset="0.6" stop-color="var(--photo-mid)"/>
        <stop offset="1" stop-color="#eef0f3"/>
      </linearGradient>
      <clipPath id="prizeDisc">
        <circle cx="631" cy="794" r="224"/>
      </clipPath>
      <filter id="prizeShadow" x="-10%" y="-10%" width="120%" height="120%">
        <feDropShadow dx="3" dy="4" stdDeviation="2" flood-color="#000" flood-opacity="0.45"/>
      </filter>
    </defs>

    <rect class="hero-photo" x="370" y="110" width="478" height="470" fill="url(#photoTone)"
          role="img" aria-label="Photo of a businessman in a dark suit pointing at survey tick boxes, with blurred colleagues behind him"/>

    <g class="headline">
      <text class="dark" x="97" y="182" font-size="160" textLength="255" lengthAdjust="spacingAndGlyphs">TAKE THE</text>
      <text class="blue" x="97" y="306" font-size="147" textLength="255" lengthAdjust="spacingAndGlyphs">SURVEY</text>
      <text class="dark" x="97" y="413" font-size="111" textLength="255" lengthAdjust="spacingAndGlyphs">ENTER THE</text>
      <text class="blue" x="97" y="506" font-size="107" textLength="255" lengthAdjust="spacingAndGlyphs">COMPETETION</text>
      <text class="dark" x="97" y="624" font-size="146" textLength="255" lengthAdjust="spacingAndGlyphs">BECOME</text>
      <line class="headline-rule" x1="97" y1="644" x2="350" y2="644"/>
      <text class="blue" x="99" y="730" font-size="97" textLength="251" lengthAdjust="spacingAndGlyphs">THE WINNER</text>
      <line class="headline-rule" x1="97" y1="745" x2="350" y2="745"/>
    </g>

    <g class="prize-badge">
      <g clip-path="url(#prizeDisc)">
        <circle cx="631" cy="794" r="224" fill="var(--brand-blue)"/>
        <polygon points="400,998 848,869 848,1100 400,1100" fill="var(--prize-yellow)"/>
      </g>
      <g class="prize-text" filter="url(#prizeShadow)" fill="var(--paper)">
        <text x="628" y="738" font-size="122" text-anchor="middle" textLength="214" lengthAdjust="spacingAndGlyphs" transform="rotate(-16 628 738)">WIN</text>
        <text x="650" y="870" font-size="140" text-anchor="middle" textLength="275" lengthAdjust="spacingAndGlyphs" transform="rotate(-16 650 870)">$200</text>
      </g>
      <text class="prize-text" x="700" y="972" font-size="50" fill="var(--ink)" text-anchor="middle" textLength="135" lengthAdjust="spacingAndGlyphs" transform="rotate(-16 700 972)">CASH</text>
    </g>
  </svg>

  <p class="survey-purpose">The survey is for determining a market for rostering and payroll software, your assistance in taking this survey would be greatly appreciated. <span class="survey-purpose__sign">– Martin Hale</span></p>

  <section class="survey-panel">
    <p class="survey-panel__intro">Complete our<br>online survey at</p>
    <p class="survey-panel__url">www.TandemRoster.com.au</p>
  </section>

  <section class="closing">
    <p class="closing__date"><strong>Closing Date</strong> xx-xx-xxxx</p>
    <p class="closing__note">Winning Contestant will be Informed by Phone</p>
  </section>

  <div class="footer-band"></div>
</main>
</body>
</html>
```